tile distributor needs a new logo and packaging designe

"VALDRIK TILE & STONE LTD'' in Canada needs great logo and a graphic design for a cardboard box package for the ceramic tiles. For inspiration you can use the logo from our sister's company, www.valdrik-fliesen.de.
In regards to the cardboard package for the ceramic tiles it should include the VALDRIK new logo on white cardboard background.
The box has to have the following info:
-Company name (with slogan "ARCHITECTURAL SOLUTIONS" or similar)
-Nominal size of the tiles (we need packages for 30cm x 60cm, 60cm x 60cm,and 30cm x 90cm) with table: nominal thickness, #pieces per box and MQ/SFT per box
-product description "RECTIFIED PORCELAIN TILE"
-made in china (not too visible, small letters)
-CE sign
-Attention text:"Before tile setting, please verify...." (see the attachment)
-Emission in indoor air sign
-and the hole on the front page (the color of the tile should be visible)
All text will be translated in 3 languages (German, English and Serbian)
I have attached some samples of the competitor"s packages and our current box for your reference.
Updates
I have increased the budget for CND$100 for my project and I hope that now it will be more atractiv for designers.
Looking forward to seeing your fresh ideas.
Project Deadline Extended
Reason: I have just increased the budget for this project therefore I am extending the deadline.
Hope this will help to get the great design for my company logo and packaging.
Industry/Entity Type
Graphic Design
Look and feel
Each slider illustrates characteristics of the customer's brand and the style your logo design should communicate.

```html
<!DOCTYPE html>
<html lang="en">
<head>
<meta charset="utf-8">
<title>Valdrik Tile &amp; Stone – Tile Box Dieline</title>
<link rel="stylesheet" href="https://fonts.googleapis.com/css2?family=Archivo:ital,wght@0,400;0,600;0,700;1,800&display=swap">
<style>
  :root {
    --page: #eceeef;
    --board: #ffffff;
    --blue-light: #1b6fb5;
    --blue-flap: #1a73b8;
    --blue-dark: #2b3a8f;
    --ink: #1c1c1f;
    --rule: #3d8fd0;
    --tile: #c8b09a;
  }
  html, body {
    margin: 0;
    width: 1200px;
    height: 783px;
    overflow: hidden;
    background: var(--page);
    font-family: "Archivo", Arial, sans-serif;
  }
  .dieline {
    position: absolute;
    left: 183px;
    top: 33px;
    width: 538px;
    height: 462px;
    transform: scale(1.55);
    transform-origin: 0 0;
  }
  .part { position: absolute; }
  .flap-left  { left: 0;     top: 43px; width: 47px;  height: 377px; background: var(--blue-flap); }
  .band-left  { left: 47px;  top: 0;    width: 32px;  height: 462px; background: var(--blue-light); }
  .front      { left: 79px;  top: 0;    width: 380px; height: 462px; background: var(--board); }
  .band-right { left: 459px; top: 0;    width: 32px;  height: 462px; background: var(--blue-dark); }
  .flap-right { left: 491px; top: 43px; width: 47px;  height: 377px; background: var(--blue-dark); }

  .rot90 { position: absolute; transform: rotate(90deg); transform-origin: 0 0; white-space: nowrap; }
  .rot180 { position: absolute; transform: rotate(180deg); white-space: nowrap; }

  .size-label { font-weight: 800; font-style: italic; color: var(--blue-dark); }
  .flap-left .size-label, .flap-right .size-label { color: #fff; font-size: 8px; }

  /* brand wordmark: one weight, one colour, plain square beside it */
  .wordmark { display: flex; align-items: center; gap: 6px; color: var(--ink); font-weight: 600; }
  .wordmark .square { flex: none; background: var(--blue-light); }
  .tagline { font-weight: 400; color: var(--blue-dark); letter-spacing: .08em; }

  .flap-name { left: 30px; top: 52px; color: #fff; }
  .flap-name .name { font-weight: 600; font-size: 6px; }
  .flap-name .tagline { color: #fff; font-size: 4px; }
  .flap-left .recycle { position: absolute; left: 13px; top: 177px; }
  .flap-left .size-label { left: 30px; top: 297px; }

  .top-size { left: 14px; top: 10px; font-size: 8px; }
  .top-recycle { position: absolute; left: 153px; top: 8px; transform: rotate(180deg); }
  .top-brand { left: 250px; top: 6px; text-align: right; }
  .top-brand .wordmark { font-size: 5px; gap: 3px; }
  .top-brand .square { width: 6px; height: 6px; }
  .top-brand .tagline { font-size: 3px; }

  .brand-block { position: absolute; left: 16px; top: 150px; width: 350px; text-align: center; }
  .brand-block .wordmark { justify-content: center; font-size: 21px; margin: 0; }
  .brand-block .square { width: 16px; height: 16px; }
  .brand-block .tagline { font-size: 11px; margin-top: 8px; }
  .brand-rule { position: absolute; left: 16px; top: 216px; width: 340px; height: 1px; background: var(--rule); }

  .product-band { position: absolute; left: 16px; top: 243px; width: 348px; height: 30px; background: var(--blue-dark); color: #fff; font-weight: 800; font-style: italic; font-size: 14px; line-height: 30px; text-align: center; }

  .tile-window { position: absolute; left: 16px; top: 316px; width: 69px; height: 69px; background: var(--tile); border-radius: 3px; }
  .front-size { position: absolute; left: 111px; top: 333px; font-size: 19px; }

  .spec-table { position: absolute; left: 255px; top: 317px; width: 108px; border-collapse: collapse; font-size: 5.5px; color: var(--blue-dark); }
  .spec-table td { border: 1px solid var(--blue-dark); height: 19px; padding: 0 3px; }
  .spec-table td.value { width: 26px; text-align: center; }

  .ce-mark { position: absolute; left: 16px; top: 432px; font-size: 13px; color: var(--ink); letter-spacing: -1px; }
  .origin { position: absolute; left: 86px; top: 437px; font-size: 6px; color: var(--ink); }
  .emission-badge { position: absolute; left: 192px; top: 425px; width: 54px; height: 33px; border: 1px solid #7a7a7a; box-sizing: border-box; background: linear-gradient(#fff 0 50%, #e4e4e4 50%); }
  .emission-badge::after { content: ""; position: absolute; left: 28px; top: 8px; width: 14px; height: 12px; background: #2f9a48; }
  .bottom-size { position: absolute; left: 296px; top: 438px; font-size: 8px; }

  .flap-right .size-label { left: 36px; top: 37px; }
  .notice { margin: 0; width: 58px; color: #fff; font-size: 3px; line-height: 1.35; white-space: normal; }
  .notice strong { display: block; font-size: 3.6px; }
</style>
</head>
<body>
<main class="dieline" aria-label="Valdrik Tile &amp; Stone rectified porcelain tile box, flat dieline">

  <section class="part flap-left">
    <div class="flap-name rot90">
      <div class="name">VALDRIK TILE &amp; STONE LTD</div>
      <div class="tagline">Architectural Solutions</div>
    </div>
    <svg class="recycle" width="20" height="20" viewBox="0 0 20 20" aria-label="recycling symbol" role="img">
      <g fill="none" stroke="#1c1c1f" stroke-width="2.4"><path d="M4 12 L7 6.5"/><path d="M10 4 L13 9"/><path d="M14 14 H7"/></g>
      <g fill="#1c1c1f"><path d="M7 4 L10.5 4 L8.2 7.5Z"/><path d="M15.5 10 L13.8 14 L12 10.5Z"/><path d="M4 16 L2.3 12.5 L6.3 12.8Z"/></g>
    </svg>
    <div class="size-label rot90">30 X 60 cm</div>
  </section>

  <section class="part band-left"></section>

  <section class="part front">
    <div class="top-size size-label rot180">30 X 60 cm</div>
    <svg class="top-recycle" width="20" height="20" viewBox="0 0 20 20" aria-label="recycling symbol" role="img">
      <g fill="none" stroke="#1c1c1f" stroke-width="2.4"><path d="M4 12 L7 6.5"/><path d="M10 4 L13 9"/><path d="M14 14 H7"/></g>
      <g fill="#1c1c1f"><path d="M7 4 L10.5 4 L8.2 7.5Z"/><path d="M15.5 10 L13.8 14 L12 10.5Z"/><path d="M4 16 L2.3 12.5 L6.3 12.8Z"/></g>
    </svg>
    <div class="top-brand rot180">
      <div class="wordmark"><span class="square"></span>VALDRIK TILE &amp; STONE LTD</div>
      <div class="tagline">Architectural Solutions</div>
    </div>

    <div class="brand-block">
      <h1 class="wordmark"><span class="square"></span>VALDRIK TILE &amp; STONE LTD</h1>
      <div class="tagline">Architectural Solutions</div>
    </div>
    <div class="brand-rule"></div>

    <div class="product-band">RECTIFIED PORCELAIN TILE</div>

    <div class="tile-window" role="img" aria-label="die-cut window showing the tile colour"></div>
    <div class="front-size size-label">30 X 60 cm</div>

    <table class="spec-table">
      <tr><td>pieces per box</td><td class="value">ps</td></tr>
      <tr><td>nominal thickness</td><td class="value">11mm</td></tr>
      <tr><td>MQ/SFT per box</td><td class="value">0,810</td></tr>
    </table>

    <div class="ce-mark">CE</div>
    <div class="origin">made in china</div>
    <div class="emission-badge" role="img" aria-label="emission in indoor air rating label"></div>
    <div class="bottom-size size-label">30 X 60 cm</div>
  </section>

  <section class="part band-right"></section>

  <section class="part flap-right">
    <div class="size-label rot90">30 X 60 cm</div>
    <p class="notice rot90" style="left:24px;top:127px"><strong>IMPORTANT</strong>Before tile setting please verify shade, size and surface. No claims after installation.</p>
    <p class="notice rot90" style="left:24px;top:190px"><strong>IMPORTANT</strong>Before tile setting please verify shade, size and surface. No claims after installation.</p>
    <p class="notice rot90" style="left:24px;top:253px"><strong>IMPORTANT</strong>Before tile setting please verify shade, size and surface. No claims after installation.</p>
    <p class="notice rot90" style="left:24px;top:316px"><strong>IMPORTANT</strong>Before tile setting please verify shade, size and surface. No claims after installation.</p>
  </section>

</main>
</body>
</html>
```